Flyer informing about the activities of people in action

Wege im Wandel (www.wegeimwandel-beispiel.ch) offers coaching, medation, support for traumatized people and conflict and crisis intervention. The flyer should inform about the activities in a plain and simple way (see logo on the homepage).

Target Market(s)

Adults who live in Switzerland or Germany

Requirements
Must have
• - simple flyer, the design is based on my logo. Brief information about my offer, reference to my homepage www.wegeimwandel-beispiel.
- 2-sided: on the first page - fire circle with text (see homepage - Home), on the back - offer with logo
- possibly a square flyer

Should not have
• no photos

```html
<!DOCTYPE html>
<html lang="de">
<head>
<meta charset="utf-8">
<title>Wege im Wandel – Flyer</title>
<link rel="stylesheet" href="https://fonts.googleapis.com/css2?family=Poppins:wght@300;400;500;600;700;800&display=swap">
<style>
  :root {
    --gold: #cfa50b;
    --gold-dark: #b8920a;
    --ink: #4a4a4a;
    --ink-soft: #5f5f5f;
    --paper: #f6f6f6;
    --stage: #e4e4e4;
    --rule: #c9c9c9;
    --white: #ffffff;
  }
  * { box-sizing: border-box; margin: 0; padding: 0; }
  html, body { width: 774px; height: 1200px; overflow: hidden; }
  body {
    background: var(--stage);
    font-family: "Poppins", sans-serif;
    color: var(--ink);
    position: relative;
  }
  .flyer-side {
    position: absolute;
    left: 140px;
    width: 494px;
    height: 494px;
    background: var(--paper);
    overflow: hidden;
  }
  .flyer-front { top: 82px; }
  .flyer-back { top: 622px; }

  /* ---------- front ---------- */
  .fire-ring { position: absolute; left: 0; top: 0; width: 494px; height: 494px; }
  .brand-name {
    position: absolute;
    font-weight: 600;
    color: var(--gold-dark);
    white-space: nowrap;
    display: flex;
    align-items: center;
    gap: 8px;
  }
  .brand-name .brand-dot {
    display: inline-block;
    border-radius: 50%;
    border: 2px solid var(--gold-dark);
  }
  .front-brand { left: 0; right: 0; top: 95px; justify-content: center; font-size: 27px; }
  .front-brand .brand-dot { width: 20px; height: 20px; }
  .front-headline {
    position: absolute; left: 0; right: 0; top: 195px;
    text-align: center;
  }
  .front-headline .lead {
    display: block;
    font-weight: 700;
    color: var(--gold);
    font-size: 24px;
    line-height: 28px;
  }
  .front-headline .wish {
    display: block;
    font-weight: 400;
    color: var(--ink-soft);
    font-size: 18.5px;
    line-height: 23px;
  }
  .gold-band {
    position: absolute;
    background: var(--gold);
    color: var(--white);
    font-weight: 700;
    text-align: center;
    border-radius: 8px 8px 0 0;
    box-shadow: 0 7px 8px -4px rgba(80, 70, 110, 0.45);
  }
  .front-band { left: 68px; width: 358px; top: 283px; height: 32px; font-size: 22px; line-height: 33px; }
  .front-context {
    position: absolute; left: 0; right: 0; top: 338px;
    text-align: center;
    font-weight: 400;
    color: var(--ink-soft);
    font-size: 14.5px;
    line-height: 16.5px;
  }

  /* ---------- back ---------- */
  .back-title {
    position: absolute; left: 0; right: 0; top: 19px;
    text-align: center;
    font-weight: 700;
    font-size: 16px;
    color: var(--ink);
    letter-spacing: -0.2px;
  }
  .back-band { left: 22px; width: 441px; top: 41px; height: 32px; font-size: 15.5px; line-height: 33px; }
  .offer {
    position: absolute; left: 0; right: 0;
  }
  .offer-icon {
    position: absolute; left: 35px; top: 0;
    width: 57px; height: 57px;
    border-radius: 50%;
    border: 2px solid var(--gold);
    background: #faf6e6;
  }
  .offer-text { position: absolute; left: 109px; right: 22px; top: 0; }
  .offer-title {
    font-weight: 700;
    color: var(--gold);
    font-size: 14px;
    line-height: 15px;
    margin-bottom: 5px;
  }
  .offer-summary {
    font-weight: 600;
    font-size: 9.3px;
    line-height: 13.4px;
    color: var(--ink-soft);
    margin-bottom: 4px;
  }
  .offer-detail {
    font-weight: 400;
    font-size: 9.3px;
    line-height: 13.4px;
    color: #6a6a6a;
  }
  .offer-coaching { top: 95px; }
  .offer-coaching .offer-icon { top: -5px; }
  .offer-mediation { top: 196px; }
  .offer-mediation .offer-icon { top: -9px; }
  .offer-trauma { top: 311px; }
  .offer-trauma .offer-icon { top: -6px; }
  .divider {
    position: absolute; left: 22px; width: 441px; height: 1px;
    background: var(--rule);
  }
  .divider-one { top: 178px; }
  .divider-two { top: 294px; }
  .back-brand { left: 35px; top: 425px; font-size: 19px; }
  .back-brand .brand-dot { width: 15px; height: 15px; }
  .web-band {
    position: absolute; left: 205px; right: 0; top: 443px; height: 29px;
    background: var(--gold);
    border-radius: 15px 0 0 15px;
    display: flex; align-items: center;
    padding-left: 18px;
    color: var(--white);
    font-size: 12px;
    gap: 10px;
    white-space: nowrap;
  }
  .web-band strong { font-weight: 700; }
  .web-band svg { flex: none; }
</style>
</head>
<body>

<section class="flyer-side flyer-front">
  <svg class="fire-ring" viewBox="0 0 494 494" aria-hidden="true">
    <circle cx="258" cy="245" r="214" fill="none" stroke="#cfa50b" stroke-width="9"/>
    <circle cx="262" cy="243" r="226" fill="none" stroke="#cfa50b" stroke-width="3" stroke-dasharray="520 200" stroke-dashoffset="-60"/>
  </svg>
  <div class="brand-name front-brand"><span class="brand-dot"></span>Wege im Wandel</div>
  <h1 class="front-headline">
    <span class="lead">SIE MÖCHTEN</span>
    <span class="wish">IHRE BELASTENDE SITUATION LÖSEN.</span>
    <span class="wish">IHRE WICHTIGEN FRAGEN KLÄREN.</span>
  </h1>
  <div class="gold-band front-band">LEICHTER WEITERKOMMEN</div>
  <p class="front-context">IN DER FRUSTRIERENDEN<br>ZUSAMMENARBEIT ODER IHREM MÜHSAMEN<br>(ZUSAMMEN-)LEBEN.</p>
</section>

<section class="flyer-side flyer-back">
  <h2 class="back-title">ICH BEGLEITE SIE UND BRINGE IHNEN</h2>
  <div class="gold-band back-band">ORIENTIERUNG, KLARHEIT UND UNTERSTÜTZUNG.</div>

  <article class="offer offer-coaching">
    <div class="offer-icon" role="img" aria-label="Symbol Coaching: Hand mit Megafon"></div>
    <div class="offer-text">
      <h3 class="offer-title">COACHING</h3>
      <p class="offer-summary">Manchmal braucht man ein Gegenüber zum Klären der eigenen Situation oder beim Entdecken neuer Sichtweisen und Handlungsmöglichkeiten.</p>
      <p class="offer-detail">Mögliche Fragen: Wo stehen Sie heute und wo wollen Sie hin? Nutzen Sie Ihre Handlungsspielräume und Ihre Fähigkeiten? Was macht Sie glücklich?</p>
    </div>
  </article>

  <div class="divider divider-one"></div>

  <article class="offer offer-mediation">
    <div class="offer-icon" role="img" aria-label="Symbol Mediation: meditierende Figur"></div>
    <div class="offer-text">
      <h3 class="offer-title">MEDIATION</h3>
      <p class="offer-summary">Gewisse Konflikte können Sie nicht mehr selber lösen. Wenige Worte entzünden einen erbitterten Streit oder erzeugen eisige Stille.</p>
      <p class="offer-detail">Mögliche Fragen: Wie finden Sie Gehör? Sehen Sie die Sichtweise Ihres Gegenübers? Wie finden Sie etwas vom verlorenen Vertrauen wieder? Wie kommen Sie wieder ins Gespräch um gemeinsam nötige Lösungen zu finden?</p>
    </div>
  </article>

  <div class="divider divider-two"></div>

  <article class="offer offer-trauma">
    <div class="offer-icon" role="img" aria-label="Symbol Begleitung: zwei Hände im Handschlag"></div>
    <div class="offer-text">
      <h3 class="offer-title">BEGLEITUNG VON<br>TRAUMATISIERTEN MENSCHEN</h3>
      <p class="offer-summary">Ihr Leben fühlt sich oft schwer, bedrückend und freudlos an. Erfolglos haben Sie probiert, sich von dieser Kontakt- und Perspektivlosigkeit zu befreien.</p>
      <p class="offer-detail">In dieser Begleitung geht es vorerst darum einen sicheren Rahmen zu schaffen, in dem Kontakt möglich wird und später gehalten werden kann.</p>
    </div>
  </article>

  <div class="brand-name back-brand"><span class="brand-dot"></span>Wege im Wandel</div>

  <div class="web-band">
    <svg width="15" height="15" viewBox="0 0 16 16" aria-hidden="true">
      <circle cx="8" cy="8" r="8" fill="#ffffff"/>
      <g fill="none" stroke="#cfa50b" stroke-width="1">
        <circle cx="8" cy="8" r="5"/>
        <ellipse cx="8" cy="8" rx="2.2" ry="5"/>
        <line x1="3" y1="8" x2="13" y2="8"/>
        <line x1="4" y1="5.3" x2="12" y2="5.3"/>
        <line x1="4" y1="10.7" x2="12" y2="10.7"/>
      </g>
    </svg>
    <span>www.<strong>wegeimwandel-beispiel</strong>.ch</span>
  </div>
</section>

</body>
</html>
```